PowerPoint Design Project

We are looking for a corporate presentation design (example content provided on approximately 30 slides).

The design will be a corporate design for our brand: VRAN
Continental Travel Planners Guild
For brand colours, requirements and logo look at: www.vran-guild.example/media
or check the attached documents. We need to incorporate logo and brand but we are happy to refresh the palette. Attached please also find designs and colour palette of our new website-presentation should complement these.

You are also free to use photos from events some of which can be found here:
http://www.socialnet.example/pages/Continental-Travel-Planners-Guild/402915736480193?sk=photos_stream

Most important:
-PROFESSIONAL AUDIENCE-PROFESSIONAL DESIGN
-SIMPLE (see example our homepage in attachment)
-ADDED SIMPLE ANIMATIONS

-DESIGN TO BE DONE ON THE EXAMPLE PRESENTATION BUT TO BE RE-USABLE FOR OTHER PRESENTATIONS
Updates

Hi, we have just uploaded our corporate social media icons which could be added on contact/end slide and on the welcome slide.

Hi all, 

-I uploaded a new high res version of the map which can be included in your designs (feel free to change colour scheme)
-Also amended upload of the Plexo + social media icon

Reason: I am looking forward to seeing a couple more designs. Please try including some suggested animations.

Target Market(s)

Presentation will be B2B and most audience are representatives of various companies in the tourism industry (tour operators, tourist boards, hotels )

Industry/Entity Type

Events

Requirements
Must have
• sleek graphics design
Nice to have
• animations

```html
<!DOCTYPE html>
<html lang="en">
<head>
<meta charset="utf-8">
<title>VRAN – Presentation Template</title>
<link href="https://fonts.googleapis.com/css2?family=PT+Sans:wght@400;700&display=swap" rel="stylesheet">
<style>
  :root{
    --navy:#2b3170;
    --ribbon:#11173a;
    --slide-bg:#e5e6e8;
    --map-tone:#d6d8dc;
    --yellow:#ffe14f;
    --accent:#5b8fd0;
    --mid-blue:#2d3a7c;
    --grey-text:#7b7c80;
    --white:#ffffff;
    --row-a:#c9cacd;
    --row-b:#e2e3e5;
  }
  *{box-sizing:border-box;margin:0;padding:0}
  html,body{width:1200px;height:1000px;overflow:hidden;background:var(--white)}
  body{position:relative;font-family:"PT Sans",Arial,sans-serif;color:var(--grey-text)}

  .slide{position:absolute;width:380px;height:286px;background:var(--slide-bg);overflow:hidden;
    box-shadow:0 1px 3px rgba(0,0,0,.35);border-bottom:4px solid var(--yellow)}
  .slide-header{position:absolute;left:0;top:0;width:100%;height:37px;background:var(--navy)}
  .slide-title{position:absolute;left:10px;top:7px;color:var(--white);font-size:17px;font-weight:400}
  .brand-ribbon{position:absolute;top:0}
  .brand-ribbon svg{display:block}
  .brand-name{position:absolute;left:0;width:100%;text-align:center;color:var(--white);font-size:10px;letter-spacing:.5px}
  .map-area{position:absolute;background:linear-gradient(135deg,var(--map-tone),var(--slide-bg));opacity:.8}

  .hero-band{position:absolute;left:0;top:0;width:100%;height:142px;background:var(--navy)}
  .hero-title{position:absolute;left:120px;top:58px;color:var(--white);font-size:17px;line-height:21px;font-weight:400}
  .hero-meta{position:absolute;left:15px;top:202px;font-size:12px;line-height:17px}

  .timeline{position:absolute;left:0;top:152px;width:100%;height:15px;
    background:linear-gradient(#f3f3f4,#a9abb0 60%,#c8c9cd)}
  .fact-box{position:absolute;background:var(--white);border:1px solid #b9bbc0;font-size:9.5px;
    line-height:12px;color:#333;text-align:center;display:flex;align-items:center;justify-content:center;padding:3px}
  .fact-box span{display:block}
  .fact-box em{font-style:normal;color:var(--accent)}

  .section-sub{position:absolute;left:10px;top:45px;color:var(--navy);font-weight:700;font-size:12.5px}
  .bullet-list{position:absolute;left:10px;top:71px;list-style:none;font-size:11.5px}
  .bullet-list li{height:25px}
  .bullet-list li::before{content:"•";color:var(--accent);margin-right:8px}
  .bullet-list .sub{padding-left:18px;font-size:10px;margin-top:-6px}
  .bullet-list .sub::before{content:"–";color:var(--navy)}
  .photo-frame{position:absolute;left:236px;top:78px;width:110px;height:152px;background:var(--white);padding:4px;
    box-shadow:0 1px 3px rgba(0,0,0,.4)}
  .photo-frame div{width:100%;height:100%;background:linear-gradient(160deg,#8fb8e6,#1f4f86 60%,#0f2c55)}

  .bubble-text{position:absolute;left:110px;top:120px;width:170px;text-align:center;color:var(--white);font-size:14px;line-height:17px}

  .content-title{position:absolute;left:0;width:100%;text-align:center}
  .content-title.bold{color:var(--navy);font-weight:700;font-size:15px;top:63px}
  .content-title.light{color:#6d6e72;font-weight:400;font-size:15px;top:63px}
  .content-desc{position:absolute;left:0;top:86px;width:100%;text-align:center;font-size:9.5px}
  .data-table{position:absolute;left:62px;top:122px;border-collapse:collapse;font-size:9px;color:#333}
  .data-table th{background:var(--navy);color:var(--white);font-weight:700;padding:2px 0;width:63px;border:1px solid var(--white)}
  .data-table td{text-align:center;padding:2px 0;border:1px solid var(--white)}
  .data-table tr:nth-child(odd) td{background:var(--row-b)}
  .data-table tr:nth-child(even) td{background:var(--row-a)}
  .chart-card{position:absolute;background:var(--white);box-shadow:0 0 2px rgba(0,0,0,.3)}

  .thanks-bar{position:absolute;left:155px;top:155px;width:225px;height:25px;background:var(--yellow);
    color:#1a1a1a;font-size:12px;padding:5px 0 0 10px}
  .contact{position:absolute;left:165px;top:203px;font-size:8.5px;line-height:11px}
  .contact b{color:var(--navy);font-weight:400}
  .social-row{position:absolute;left:165px;top:250px;display:flex;gap:4px}
  .social-row span{width:18px;height:18px;background:var(--ribbon)}
</style>
</head>
<body>

<!-- 1 Title -->
<section class="slide" style="left:15px;top:48px">
  <div class="hero-band"></div>
  <div class="map-area" role="img" aria-label="Dotted map of Europe" style="left:270px;top:150px;width:110px;height:132px"></div>
  <div class="brand-ribbon" style="left:42px">
    <svg width="60" height="168"><polygon points="0,0 60,0 60,152 0,168" fill="var(--ribbon)"/></svg>
    <span class="brand-name" style="top:76px;font-size:14px">VRAN</span>
  </div>
  <h1 class="hero-title">Continental Travel Planners<br>Guild (VRAN)</h1>
  <p class="hero-meta">12.02.2013<br>Harbourview Arena</p>
</section>

<!-- 2 Quick facts -->
<section class="slide" style="left:410px;top:48px">
  <div class="slide-header"></div>
  <h2 class="slide-title">Quick Facts</h2>
  <div class="brand-ribbon" style="left:312px">
    <svg width="60" height="67"><polygon points="0,0 60,0 60,55 0,67" fill="var(--ribbon)"/></svg>
    <span class="brand-name" style="top:26px">VRAN</span>
  </div>
  <div class="map-area" role="img" aria-label="Dotted map of Europe" style="left:270px;top:150px;width:110px;height:132px"></div>
  <div class="timeline"></div>
  <svg style="position:absolute;left:0;top:120px" width="380" height="140">
    <g fill="var(--accent)">
      <polygon points="32,36 38,40 32,44"/><polygon points="42,36 48,40 42,44"/><polygon points="52,36 58,40 52,44"/>
      <polygon points="120,36 126,40 120,44"/><polygon points="130,36 136,40 130,44"/><polygon points="140,36 146,40 140,44"/>
      <polygon points="218,36 224,40 218,44"/><polygon points="228,36 234,40 228,44"/><polygon points="238,36 244,40 238,44"/>
      <polygon points="310,36 316,40 310,44"/><polygon points="320,36 326,40 320,44"/><polygon points="330,36 336,40 330,44"/>
    </g>
    <g stroke="var(--accent)" stroke-width="1" fill="var(--accent)">
      <line x1="48" y1="6" x2="48" y2="30"/><circle cx="48" cy="30" r="2.5"/>
      <line x1="233" y1="6" x2="233" y2="30"/><circle cx="233" cy="30" r="2.5"/>
      <line x1="134" y1="50" x2="134" y2="83"/><circle cx="134" cy="50" r="2.5"/>
      <line x1="325" y1="50" x2="325" y2="83"/><circle cx="325" cy="50" r="2.5"/>
    </g>
  </svg>
  <div class="fact-box" style="left:6px;top:82px;width:88px;height:44px"><span>Established<br>since <em>1989</em></span></div>
  <div class="fact-box" style="left:186px;top:82px;width:92px;height:44px"><span>Members located<br>in <em>35</em> countries<br>worldwide</span></div>
  <div class="fact-box" style="left:90px;top:203px;width:88px;height:40px"><span><em>600</em> Members</span></div>
  <div class="fact-box" style="left:282px;top:203px;width:88px;height:40px"><span><em>€5.5bn</em> in product<br>purchasing</span></div>
</section>

<!-- 3 Bullets -->
<section class="slide" style="left:806px;top:48px">
  <div class="slide-header"></div>
  <h2 class="slide-title">Why B2B marketing?</h2>
  <div class="brand-ribbon" style="left:312px">
    <svg width="60" height="67"><polygon points="0,0 60,0 60,55 0,67" fill="var(--ribbon)"/></svg>
    <span class="brand-name" style="top:26px">VRAN</span>
  </div>
  <h3 class="section-sub">B2B marketing know-how</h3>
  <ul class="bullet-list">
    <li>B2B website</li>
    <li>E-marketing campaigns</li>
    <li>Fam trips and travel trade events</li>
    <li>Travel trade events</li>
    <li>Other options</li>
    <li class="sub">sponsorship</li>
  </ul>
  <div class="photo-frame"><div role="img" aria-label="Photo of a glass office tower against a blue sky"></div></div>
</section>

<!-- 4 Question -->
<section class="slide" style="left:15px;top:363px">
  <div class="slide-header"></div>
  <h2 class="slide-title">Why B2B marketing?</h2>
  <div class="brand-ribbon" style="left:310px">
    <svg width="60" height="67"><polygon points="0,0 60,0 60,55 0,67" fill="var(--ribbon)"/></svg>
    <span class="brand-name" style="top:26px">VRAN</span>
  </div>
  <div class="map-area" role="img" aria-label="Dotted map of Europe" style="left:270px;top:100px;width:110px;height:182px"></div>
  <h3 class="section-sub">B2B Website</h3>
  <svg style="position:absolute;left:70px;top:60px" width="230" height="210">
    <path d="M115,8 C175,8 218,45 218,88 C218,132 175,168 115,168 C105,168 98,167 92,166 L68,204 L76,160 C38,148 12,120 12,88 C12,45 55,8 115,8 Z"
      fill="var(--navy)" stroke="var(--white)" stroke-width="2.5"/>
  </svg>
  <p class="bubble-text">How many suppliers<br>in the room have a<br>trade-specific<br>website?</p>
</section>

<!-- 5 Table -->
<section class="slide" style="left:415px;top:363px">
  <div class="slide-header"></div>
  <h2 class="slide-title">Table slide</h2>
  <div class="brand-ribbon" style="left:310px">
    <svg width="60" height="67"><polygon points="0,0 60,0 60,55 0,67" fill="var(--ribbon)"/></svg>
    <span class="brand-name" style="top:26px">VRAN</span>
  </div>
  <div class="map-area" role="img" aria-label="Dotted map of Europe" style="left:270px;top:150px;width:110px;height:132px"></div>
  <h3 class="content-title bold">Table title</h3>
  <p class="content-desc">Small description of the table contents and its conclusions</p>
  <table class="data-table">
    <tr><th>Category A</th><th>Category B</th><th>Category C</th><th>Category D</th></tr>
    <tr><td>111.333</td><td>111.555</td><td>111.333</td><td>111.555</td></tr>
    <tr><td>444.555</td><td>444.333</td><td>444.555</td><td>444.333</td></tr>
    <tr><td>111.222</td><td>222.333</td><td>111.222</td><td>222.333</td></tr>
    <tr><td>222.555</td><td>555.333</td><td>222.555</td><td>555.333</td></tr>
    <tr><td>333.444</td><td>333.111</td><td>333.444</td><td>333.111</td></tr>
  </table>
</section>

<!-- 6 Bar chart -->
<section class="slide" style="left:806px;top:363px">
  <div class="slide-header"></div>
  <h2 class="slide-title">Chart slide</h2>
  <div class="brand-ribbon" style="left:315px">
    <svg width="60" height="67"><polygon points="0,0 60,0 60,55 0,67" fill="var(--ribbon)"/></svg>
    <span class="brand-name" style="top:26px">VRAN</span>
  </div>
  <div class="map-area" role="img" aria-label="Dotted map of Europe" style="left:270px;top:150px;width:110px;height:132px"></div>
  <h3 class="content-title light">Chart title</h3>
  <p class="content-desc">Small description of the chart contents and its conclusions</p>
  <div class="chart-card" style="left:52px;top:104px;width:282px;height:160px">
    <svg width="282" height="160" font-family="PT Sans, Arial, sans-serif" font-size="7.5" fill="#666" text-anchor="middle">
      <line x1="12" y1="120" x2="274" y2="120" stroke="#ccc"/>
      <g>
        <rect x="25" y="34" width="13" height="86" fill="var(--ribbon)"/><text x="31.5" y="30">4,3</text>
        <rect x="38" y="72" width="13" height="48" fill="var(--mid-blue)"/><text x="44.5" y="68">2,4</text>
        <rect x="51" y="80" width="13" height="40" fill="var(--accent)"/><text x="57.5" y="76">2</text>
        <text x="44.5" y="132">Category 1</text>
      </g>
      <g>
        <rect x="89" y="70" width="13" height="50" fill="var(--ribbon)"/><text x="95.5" y="66">2,5</text>
        <rect x="102" y="32" width="13" height="88" fill="var(--mid-blue)"/><text x="108.5" y="28">4,4</text>
        <rect x="115" y="80" width="13" height="40" fill="var(--accent)"/><text x="121.5" y="76">2</text>
        <text x="108.5" y="132">Category 2</text>
      </g>
      <g>
        <rect x="153" y="50" width="13" height="70" fill="var(--ribbon)"/><text x="159.5" y="46">3,5</text>
        <rect x="166" y="84" width="13" height="36" fill="var(--mid-blue)"/><text x="172.5" y="80">1,8</text>
        <rect x="179" y="60" width="13" height="60" fill="var(--accent)"/><text x="185.5" y="56">3</text>
        <text x="172.5" y="132">Category 3</text>
      </g>
      <g>
        <rect x="213" y="30" width="13" height="90" fill="var(--ribbon)"/><text x="219.5" y="26">4,5</text>
        <rect x="226" y="64" width="13" height="56" fill="var(--mid-blue)"/><text x="232.5" y="60">2,8</text>
        <rect x="239" y="20" width="13" height="100" fill="var(--accent)"/><text x="245.5" y="16">5</text>
        <text x="232.5" y="132">Category 4</text>
      </g>
      <g text-anchor="start">
        <rect x="86" y="140" width="4" height="4" fill="var(--ribbon)"/><text x="93" y="144.5">Series 1</text>
        <rect x="126" y="140" width="4" height="4" fill="var(--mid-blue)"/><text x="133" y="144.5">Series 2</text>
        <rect x="166" y="140" width="4" height="4" fill="var(--accent)"/><text x="173" y="144.5">Series 3</text>
      </g>
    </svg>
  </div>
</section>

<!-- 7 Donut chart -->
<section class="slide" style="left:15px;top:688px">
  <div class="slide-header"></div>
  <h2 class="slide-title">Pie chart slide</h2>
  <div class="brand-ribbon" style="left:305px">
    <svg width="60" height="67"><polygon points="0,0 60,0 60,55 0,67" fill="var(--ribbon)"/></svg>
    <span class="brand-name" style="top:26px">VRAN</span>
  </div>
  <div class="map-area" role="img" aria-label="Dotted map of Europe" style="left:270px;top:150px;width:110px;height:132px"></div>
  <h3 class="content-title light">Chart title</h3>
  <p class="content-desc">Small description of the chart contents and its conclusions</p>
  <div class="chart-card" style="left:52px;top:103px;width:272px;height:152px">
    <svg width="272" height="152" font-family="PT Sans, Arial, sans-serif" font-size="7.5" fill="#666">
      <g transform="translate(134,72) rotate(-90)" fill="none" stroke-width="32">
        <circle r="46" stroke="var(--ribbon)" stroke-dasharray="136 289"/>
        <circle r="46" stroke="var(--mid-blue)" stroke-dasharray="0 136 64 289"/>
        <circle r="46" stroke="var(--accent)" stroke-dasharray="0 200 55 289"/>
        <circle r="46" stroke="var(--yellow)" stroke-dasharray="0 255 34 289"/>
      </g>
      <rect x="66" y="141" width="4" height="4" fill="var(--ribbon)"/><text x="72" y="145.5">1st Qtr</text>
      <rect x="102" y="141" width="4" height="4" fill="var(--mid-blue)"/><text x="108" y="145.5">2nd Qtr</text>
      <rect x="139" y="141" width="4" height="4" fill="var(--accent)"/><text x="145" y="145.5">3rd Qtr</text>
      <rect x="174" y="141" width="4" height="4" fill="var(--yellow)"/><text x="180" y="145.5">4th Qtr</text>
    </svg>
  </div>
</section>

<!-- 8 Closing -->
<section class="slide" style="left:410px;top:688px">
  <div class="hero-band"></div>
  <div class="map-area" role="img" aria-label="Dotted map of Europe" style="left:195px;top:0;width:185px;height:142px;background:linear-gradient(135deg,#4d5594,var(--navy));opacity:1"></div>
  <div class="brand-ribbon" style="left:42px">
    <svg width="60" height="165"><polygon points="0,0 60,0 60,150 0,165" fill="var(--ribbon)"/></svg>
    <span class="brand-name" style="top:76px;font-size:14px">VRAN</span>
  </div>
  <div class="thanks-bar">Thanks for your attention!</div>
  <p class="contact">Find further details, please visit: <b>www.vran-guild.example</b><br>
    <b>Phone:</b> +44 20 7946 0381<br>
    <b>Email:</b> info@vran-guild.example</p>
  <div class="social-row" aria-label="Social media links">
    <span></span><span></span><span></span><span></span><span></span>
  </div>
</section>

</body>
</html>
```